Global Nano Technology Surface Protection company needs a new logo and cards

We are a Global company that will apply nanotechnology coatings on surfaces to prevent growth and spread of bacteria, viruses, mold etc. We deal with large corporates, airlines, hospitals and schools so we are after a new modern, simple and clean look that will have great visual impact.
We a company that is focused on prevention and protection.

Company name, Quorvane Systems Worldwide

Subtext, Antimicrobial Surface Protection

Logo, QVSW or QSW

Target Market(s)

Hospitals, Transport agencies, Airlines, Corporate entities

Industry/Entity Type

Protection

Contact Information for Business Card

Logo, QVSW or QSW
www.qvsw-example.us
Derek Holloway
+64290536218
tidyshieldnz@mailbox-example.com

Logo Text

QVSW

Requirements
Must have
• Simple clean look
Should not have
• Nothing too messy

```html
<!DOCTYPE html>
<html lang="en">
<head>
<meta charset="utf-8">
<title>Quorvane Systems Worldwide — Business Cards</title>
<link rel="stylesheet" href="https://fonts.googleapis.com/css2?family=Montserrat:wght@600;700&family=Questrial&display=swap">
<style>
  :root {
    --brand-blue: #0b57a8;
    --accent-blue: #3fa9e0;
    --ink: #2b2b2b;
    --muted: #6f6f6f;
    --paper: #ffffff;
    --backdrop: #e9e9e7;
  }
  * { box-sizing: border-box; margin: 0; padding: 0; }
  html, body { width: 1200px; height: 892px; overflow: hidden; }
  body {
    background: var(--backdrop);
    position: relative;
    font-family: "Questrial", sans-serif;
  }
  .card {
    position: absolute;
    top: 78px;
    width: 420px;
    height: 735px;
    box-shadow: 0 6px 18px rgba(0,0,0,0.12);
    overflow: hidden;
  }
  /* Front */
  .card-front { left: 150px; background: var(--paper); }
  .side-band {
    position: absolute; left: 0; top: 0; bottom: 0; width: 92px;
    background: var(--brand-blue);
  }
  .side-band-text {
    position: absolute; left: 46px; top: 367px;
    transform: translate(-50%, -50%) rotate(-90deg);
    white-space: nowrap;
    color: rgba(255,255,255,0.85);
    font-size: 38px; letter-spacing: 1px;
  }
  .front-content {
    position: absolute; left: 92px; right: 30px; top: 0; bottom: 0;
    text-align: right;
  }
  .wordmark {
    position: absolute; right: 0; top: 42px;
    display: flex; align-items: center; gap: 10px;
  }
  .wordmark-name {
    font-family: "Montserrat", sans-serif; font-weight: 700;
    font-size: 46px; color: var(--brand-blue); letter-spacing: 2px;
  }
  .wordmark-square { width: 14px; height: 14px; background: var(--brand-blue); }
  .wordmark-sub {
    position: absolute; right: 0; top: 104px;
    font-size: 11px; color: var(--muted);
  }
  .company-name {
    position: absolute; right: 0; top: 200px;
    font-family: "Montserrat", sans-serif; font-weight: 700;
    font-size: 25px; line-height: 1.3; color: var(--brand-blue);
  }
  .person { position: absolute; right: 0; top: 390px; }
  .person-name {
    font-family: "Montserrat", sans-serif; font-weight: 700;
    font-size: 25px; color: var(--ink);
  }
  .person-title { font-size: 22px; color: var(--ink); margin-top: 2px; }
  .contacts { position: absolute; right: 0; top: 540px; font-size: 16px; color: var(--ink); }
  .contact-line { display: flex; justify-content: flex-end; align-items: center; gap: 10px; margin-bottom: 22px; }
  .contact-icon { width: 18px; height: 18px; flex: none; }
  /* Back */
  .card-back { left: 630px; background: var(--brand-blue); }
  .back-mark {
    position: absolute; left: 50%; top: 46%;
    transform: translate(-50%, -50%);
    display: flex; align-items: center; gap: 8px;
  }
  .back-mark-name {
    font-family: "Montserrat", sans-serif; font-weight: 700;
    font-size: 40px; color: var(--paper); letter-spacing: 2px;
  }
  .back-mark-square { width: 12px; height: 12px; background: var(--paper); }
  .back-url {
    position: absolute; left: 0; right: 0; bottom: 50px;
    text-align: center; color: var(--paper); font-size: 17px;
  }
</style>
</head>
<body>
  <section class="card card-front">
    <div class="side-band">
      <span class="side-band-text">ANTIMICROBIAL SURFACE PROTECTION</span>
    </div>
    <div class="front-content">
      <div class="wordmark">
        <span class="wordmark-square"></span>
        <span class="wordmark-name">QVSW</span>
      </div>
      <p class="wordmark-sub">Antimicrobial Surface Protection</p>
      <h1 class="company-name">Quorvane<br>Systems<br>Worldwide</h1>
      <div class="person">
        <p class="person-name">Derek Holloway</p>
        <p class="person-title">Director</p>
      </div>
      <div class="contacts">
        <p class="contact-line">
          <span>+64290536218</span>
          <svg class="contact-icon" viewBox="0 0 24 24" aria-hidden="true">
            <path d="M6.6 10.8a15.1 15.1 0 0 0 6.6 6.6l2.2-2.2a1 1 0 0 1 1-.25 11.4 11.4 0 0 0 3.6.57 1 1 0 0 1 1 1V20a1 1 0 0 1-1 1A17 17 0 0 1 3 4a1 1 0 0 1 1-1h3.5a1 1 0 0 1 1 1 11.4 11.4 0 0 0 .57 3.6 1 1 0 0 1-.25 1z" fill="var(--accent-blue)"/>
          </svg>
        </p>
        <p class="contact-line">
          <span>tidyshieldnz@mailbox-example.com</span>
          <svg class="contact-icon" viewBox="0 0 24 24" aria-hidden="true">
            <rect x="2.5" y="5.5" width="19" height="13" fill="none" stroke="var(--accent-blue)" stroke-width="1.5"/>
            <path d="M2.5 5.5l9.5 7.5 9.5-7.5" fill="none" stroke="var(--accent-blue)" stroke-width="1.5"/>
          </svg>
        </p>
      </div>
    </div>
  </section>

  <section class="card card-back">
    <div class="back-mark">
      <span class="back-mark-square"></span>
      <span class="back-mark-name">QVSW</span>
    </div>
    <p class="back-url">www.qvsw-example.us</p>
  </section>
</body>
</html>
```